Marrowfield Contracting Business Cards

Front of card:

Full Logo
Name
Address
Office Phone
Cell Phone
Email
Website

Back:
Logo Mark in background
List and markets and services performed

```html
<!DOCTYPE html>
<html lang="en">
<head>
<meta charset="utf-8">
<title>Marrowfield Contracting Business Cards</title>
<link rel="stylesheet" href="https://fonts.googleapis.com/css2?family=Lato:wght@400;700;900&display=swap">
<style>
  :root {
    --backdrop: #2f3234;
    --brand-red: #d92121;
    --brand-grey: #777777;
    --paper: #ffffff;
    --ink-dark: #6b6b6b;
  }
  * { box-sizing: border-box; margin: 0; padding: 0; }
  html, body {
    width: 1200px; height: 1200px; overflow: hidden;
    background: var(--backdrop);
    font-family: "Lato", sans-serif;
  }
  .card {
    position: absolute; left: 250px; width: 700px; height: 399px;
    border-radius: 32px; overflow: hidden;
  }
  .card-front { top: 170px; background: var(--brand-red); }
  .card-back { top: 631px; background: var(--brand-grey); }

  .front-panel { position: absolute; inset: 0; }

  .contact-block { position: absolute; left: 35px; top: 76px; color: var(--paper); }
  .person-name { font-weight: 900; font-size: 31px; letter-spacing: 0.2px; line-height: 1; }
  .person-title { font-size: 20px; margin-top: 6px; }
  .contact-list { list-style: none; margin-top: 10px; font-size: 17px; }
  .contact-list li { display: flex; align-items: flex-start; gap: 12px; line-height: 24.5px; }
  .contact-list svg { width: 14px; height: 14px; flex: none; margin-top: 5px; fill: var(--paper); }

  .brand-lockup {
    position: absolute; left: 348px; top: 175px; width: 330px;
    display: flex; align-items: center; gap: 12px;
  }
  .brand-dot { width: 44px; height: 44px; border-radius: 50%; background: var(--brand-red); flex: none; }
  .brand-name {
    color: var(--brand-red); font-weight: 700; font-size: 23px;
    text-transform: uppercase; letter-spacing: 1px; line-height: 1.1;
  }

  .back-brand {
    position: absolute; left: 60px; top: 0; height: 399px; width: 260px;
    display: flex; flex-direction: column; align-items: center; justify-content: center; gap: 16px;
  }
  .back-brand .brand-dot { width: 90px; height: 90px; background: var(--paper); }
  .back-brand .brand-name { color: var(--paper); font-size: 24px; text-align: center; }

  .divider { position: absolute; left: 362px; top: 76px; width: 1px; height: 247px; background: #d8d8d8; }

  .services { position: absolute; left: 400px; top: 74px; color: var(--paper); }
  .services-heading { font-weight: 900; font-size: 27px; line-height: 1; margin-bottom: 6px; }
  .services-list { list-style: none; font-size: 17px; }
  .services-list li { line-height: 24.5px; position: relative; padding-left: 19px; }
  .services-list li::before {
    content: ""; position: absolute; left: 0; top: 10px;
    width: 6px; height: 6px; border-radius: 50%; background: var(--paper);
  }
</style>
</head>
<body>

<section class="card card-front" aria-label="Card front">
  <svg class="front-panel" viewBox="0 0 700 399" width="700" height="399" aria-hidden="true">
    <circle cx="505" cy="200" r="216" fill="var(--paper)"/>
    <rect x="505" y="0" width="195" height="399" fill="var(--paper)"/>
  </svg>

  <div class="contact-block">
    <h1 class="person-name">DANIEL HARLOW</h1>
    <p class="person-title">Founder &amp; CEO</p>
    <ul class="contact-list">
      <li><svg viewBox="0 0 14 14"><path d="M7 0a5 5 0 0 0-5 5c0 3.5 5 9 5 9s5-5.5 5-9a5 5 0 0 0-5-5zm0 7a2 2 0 1 1 0-4 2 2 0 0 1 0 4z"/></svg><span>Address, City, State<br>Country, Zip Code 01235</span></li>
      <li><svg viewBox="0 0 14 14"><path d="M3 0l2.5 3-1.5 2c1 2 3 4 5 5l2-1.5 3 2.5-1.5 2.5C7 14 0 7 .5 1.5z"/></svg><span>(555) 218-4630</span></li>
      <li><svg viewBox="0 0 14 14"><path d="M3.5 0h7v14h-7zM5 1.5v9.5h4V1.5zM6.3 12h1.4v1H6.3z" fill-rule="evenodd"/></svg><span>(555) 218-4631</span></li>
      <li><svg viewBox="0 0 14 14"><path d="M3 0h8v4H3zM1 5h12v6h-2v3H3v-3H1zM4.5 9v3.5h5V9z" fill-rule="evenodd"/></svg><span>(555) 218-4632</span></li>
      <li><svg viewBox="0 0 14 14"><path d="M0 2.5h14v9H0zM1 3.5l6 4.5 6-4.5" /></svg><span>office@marrowfieldco.com</span></li>
      <li><svg viewBox="0 0 14 14"><circle cx="7" cy="7" r="7"/></svg><span>www.marrowfieldco.com</span></li>
    </ul>
  </div>

  <div class="brand-lockup">
    <span class="brand-dot"></span>
    <span class="brand-name">Marrowfield<br>Contracting</span>
  </div>
</section>

<section class="card card-back" aria-label="Card back">
  <div class="back-brand">
    <span class="brand-dot"></span>
    <span class="brand-name">Marrowfield<br>Contracting</span>
  </div>
  <div class="divider"></div>
  <div class="services">
    <h2 class="services-heading">OUR SERVICES</h2>
    <ul class="services-list">
      <li>Lorem ipsum</li>
      <li>Aliquam tincidunt</li>
      <li>Vestibulum auctor</li>
      <li>Nunc dignissim</li>
      <li>Cras ornare</li>
      <li>Vivamus vestibulum</li>
      <li>Praesent placerat</li>
      <li>Fusce pellentesque</li>
      <li>Integer vitae</li>
    </ul>
  </div>
</section>

</body>
</html>
```